Prickly Heat Powder

prickly heat powders are used in summers to provide cooling effect to body and relief body from heat effects during summers.

we have 4 variants of prickly heat.

1) Menthol
2) Rose
3) Lemon
4) Neem

Bottle is in round cylinder shape. It also has a cap. Will share pictures of bottle and cap tomorrow.

Brand Name is KAVELO.

Total label size will be 180mm width * 140mm height. But main design will be small because bottle is round.

Target Market(s)

B Class.
C plus and C.
Masses

Industry/Entity Type

Cosmetics

Requirements
Must have
• icy effect, joyful and playful
Nice to have
• joyful and eye catching designs. more colors would be good.
• Polar bear might look nice.
• Kavelo Logo to be bold and prominent.

```html
<!DOCTYPE html>
<html lang="en">
<head>
<meta charset="utf-8">
<title>Kavelo Prickly Heat Cooling Powder – Labels</title>
<link rel="stylesheet" href="https://fonts.googleapis.com/css2?family=Didact+Gothic&display=swap">
<style>
  :root {
    --page-bg: #ffffff;
    --ink: #3a3a3c;
    --ink-soft: #4a4a4e;
    --rose-deep: #f2a3aa;
    --rose-mid: #f6c3cc;
    --rose-light: #fae3ea;
    --rose-rule: #ea8ca0;
    --mint-deep: #bfe2f5;
    --mint-mid: #d6ecf8;
    --mint-light: #e8f3fa;
    --mint-rule: #6cc3e6;
    --silver: #d9d9de;
    --silver-light: #f4f4f6;
  }
  * { margin: 0; padding: 0; box-sizing: border-box; }
  html, body {
    width: 1200px; height: 1184px; overflow: hidden;
    background: var(--page-bg);
    font-family: "Didact Gothic", "Helvetica Neue", Arial, sans-serif;
    color: var(--ink);
  }
  .canvas {
    position: relative; width: 1200px; height: 1184px;
    display: flex; justify-content: center; align-items: center; gap: 84px;
  }
  .label {
    position: relative; width: 300px; height: 530px; overflow: hidden;
  }
  .label__art { position: absolute; inset: 0; width: 100%; height: 100%; }
  .brand {
    position: absolute; left: 14px; top: 30px;
    font-size: 58px; line-height: 1; color: var(--ink); letter-spacing: 0.5px;
  }
  .product-name {
    position: absolute; left: 30px; right: 28px; top: 196px;
    font-size: 39px; line-height: 1; text-align: center; color: var(--ink-soft);
  }
  .product-type {
    position: absolute; left: 30px; right: 28px; top: 247px;
    padding: 7px 0 6px;
    border-top: 3px solid var(--rule); border-bottom: 3px solid var(--rule);
    font-size: 23px; line-height: 1.1; text-align: center; color: var(--ink-soft);
  }
  .label--rose { --rule: var(--rose-rule); }
  .label--mint { --rule: var(--mint-rule); }
  .claim {
    position: absolute; left: 30px; top: 328px;
    font-size: 16.5px; line-height: 22px; color: var(--ink-soft);
  }
  .variant-badge {
    position: absolute; left: 220px; top: 420px; width: 64px; height: 64px;
    border-radius: 50%; border: 3px solid var(--silver);
    background: #ffffff;
  }
  .net-weight {
    position: absolute; left: 0; right: 0; top: 488px;
    font-size: 17px; text-align: center; color: var(--ink);
  }
</style>
</head>
<body>
<main class="canvas">

  <section class="label label--rose">
    <svg class="label__art" viewBox="0 0 300 530" aria-hidden="true">
      <defs>
        <linearGradient id="rose-bg" x1="0" y1="0" x2="1" y2="1">
          <stop offset="0" stop-color="#f5aeb3"/>
          <stop offset="1" stop-color="#ee9aa4"/>
        </linearGradient>
        <linearGradient id="rose-panel" x1="0" y1="0" x2="1" y2="0">
          <stop offset="0" stop-color="#f7d3dd"/>
          <stop offset="0.5" stop-color="#fbe6ee"/>
          <stop offset="1" stop-color="#f3cad6"/>
        </linearGradient>
      </defs>
      <rect width="300" height="530" fill="url(#rose-bg)"/>
      <path d="M0 150 C90 150 170 90 300 55 L300 425 C190 395 90 465 0 490 Z" fill="url(#rose-panel)"/>
      <path d="M0 150 C90 150 170 90 300 55" fill="none" stroke="#d8d8dd" stroke-width="7"/>
      <path d="M0 160 C95 158 175 100 300 68" fill="none" stroke="#ee8fa3" stroke-width="3"/>
      <path d="M0 490 C90 465 190 395 300 425" fill="none" stroke="#d8d8dd" stroke-width="7"/>
      <path d="M0 478 C90 452 190 382 300 410" fill="none" stroke="#ee8fa3" stroke-width="3"/>
    </svg>
    <div class="brand">Kavelo</div>
    <div class="product-name">Prickly Heat</div>
    <div class="product-type">COOLING POWDER</div>
    <p class="claim">Soothes heat rash<br>and protects from<br>skin infections</p>
    <div class="variant-badge" role="img" aria-label="Rose variant badge with a pink rose illustration" style="background: radial-gradient(circle, #f2a9bd 0 40%, #ffffff 42%);"></div>
    <div class="net-weight">150 g Net</div>
  </section>

  <section class="label label--mint">
    <svg class="label__art" viewBox="0 0 300 530" aria-hidden="true">
      <defs>
        <linearGradient id="mint-bg" x1="0" y1="0" x2="1" y2="1">
          <stop offset="0" stop-color="#c7e6f6"/>
          <stop offset="1" stop-color="#b9def3"/>
        </linearGradient>
        <linearGradient id="mint-panel" x1="0" y1="0" x2="1" y2="0">
          <stop offset="0" stop-color="#d9ecf7"/>
          <stop offset="0.5" stop-color="#e9f3fa"/>
          <stop offset="1" stop-color="#d2e7f4"/>
        </linearGradient>
      </defs>
      <rect width="300" height="530" fill="url(#mint-bg)"/>
      <path d="M0 150 C90 150 170 90 300 55 L300 425 C190 395 90 465 0 490 Z" fill="url(#mint-panel)"/>
      <path d="M0 150 C90 150 170 90 300 55" fill="none" stroke="#d8d8dd" stroke-width="7"/>
      <path d="M0 160 C95 158 175 100 300 68" fill="none" stroke="#8fd3e0" stroke-width="3"/>
      <path d="M0 490 C90 465 190 395 300 425" fill="none" stroke="#d8d8dd" stroke-width="7"/>
      <path d="M0 478 C90 452 190 382 300 410" fill="none" stroke="#8fd3e0" stroke-width="3"/>
    </svg>
    <div class="brand">Kavelo</div>
    <div class="product-name">Prickly Heat</div>
    <div class="product-type">COOLING POWDER</div>
    <p class="claim">Soothes heat rash<br>and protects from<br>skin infections</p>
    <div class="variant-badge" role="img" aria-label="Mint variant badge with green mint leaves illustration" style="background: radial-gradient(circle, #7fcaa6 0 40%, #ffffff 42%);"></div>
    <div class="net-weight">150 g Net</div>
  </section>

</main>
</body>
</html>
```